New Packaging Design Project

Wine packaging redesign. Retail partner requested a redesign of a private label wine. The old label is attached. Our partner liked the Lantern and Briar label and wanted something similar. There will be a logo added to the top of the label

Went on vacation/holiday

```html
<!DOCTYPE html>
<html lang="en">
<head>
<meta charset="utf-8">
<title>Cedar Hollow Red Blend Label</title>
<link rel="stylesheet" href="https://fonts.googleapis.com/css2?family=Cinzel:wght@500;600&family=Montserrat:wght@400;500;700&display=swap">
<style>
  :root {
    --page: #ffffff;
    --label: #2c2f36;
    --label-deep: #23262c;
    --gold: #d6a83c;
    --gold-light: #f0cf6e;
    --silver: #c9c9cb;
    --sketch-dark: #3a3d44;
    --sketch-light: #8e8f93;
  }
  * { margin: 0; padding: 0; box-sizing: border-box; }
  html, body {
    width: 1200px;
    height: 1200px;
    overflow: hidden;
    background: var(--page);
  }
  .canvas {
    position: relative;
    width: 1200px;
    height: 1200px;
  }
  .wine-label {
    position: absolute;
    left: 205px;
    top: 50px;
    width: 790px;
    height: 1100px;
    background: radial-gradient(ellipse at 50% 45%, var(--label) 0%, var(--label-deep) 100%);
    text-align: center;
    color: var(--gold);
  }
  .rating-stars {
    position: absolute;
    top: 78px;
    left: 0;
    width: 100%;
    display: flex;
    justify-content: center;
    align-items: flex-end;
    gap: 4px;
  }
  .rating-stars svg { fill: var(--gold); }
  .brand-name {
    position: absolute;
    top: 160px;
    left: 0;
    width: 100%;
    font-family: "Cinzel", serif;
    font-weight: 500;
    font-size: 76px;
    letter-spacing: 0.01em;
    color: var(--gold);
    line-height: 1;
  }
  .wine-style {
    position: absolute;
    top: 300px;
    left: 0;
    width: 100%;
    font-family: "Montserrat", sans-serif;
    font-weight: 700;
    font-size: 40px;
    letter-spacing: 0.04em;
    color: var(--gold);
    line-height: 1;
  }
  .vineyard-scene {
    position: absolute;
    top: 436px;
    left: 33px;
    width: 714px;
    height: 340px;
    border-radius: 50% / 45%;
    background: radial-gradient(ellipse at 50% 50%, var(--sketch-light) 0%, var(--sketch-dark) 70%, transparent 100%);
    opacity: 0.75;
  }
  .grape-varieties {
    position: absolute;
    top: 890px;
    left: 0;
    width: 100%;
    font-family: "Montserrat", sans-serif;
    font-weight: 500;
    font-size: 22px;
    letter-spacing: 0.2em;
    line-height: 34px;
    color: var(--gold);
  }
  .divider {
    position: absolute;
    top: 969px;
    left: 371px;
    width: 48px;
    height: 3px;
    background: var(--silver);
  }
  .vintage {
    position: absolute;
    top: 990px;
    left: 0;
    width: 100%;
    font-family: "Montserrat", sans-serif;
    font-weight: 400;
    font-size: 25px;
    letter-spacing: 0.18em;
    color: var(--silver);
  }
</style>
</head>
<body>
  <main class="canvas">
    <section class="wine-label">
      <div class="rating-stars" aria-label="Three stars">
        <svg width="28" height="28" viewBox="0 0 24 24"><path d="M12 1.5l3.1 6.9 7.4.7-5.6 5 1.7 7.4L12 17.7l-6.6 3.8 1.7-7.4-5.6-5 7.4-.7z"/></svg>
        <svg width="36" height="36" viewBox="0 0 24 24"><path d="M12 1.5l3.1 6.9 7.4.7-5.6 5 1.7 7.4L12 17.7l-6.6 3.8 1.7-7.4-5.6-5 7.4-.7z"/></svg>
        <svg width="28" height="28" viewBox="0 0 24 24"><path d="M12 1.5l3.1 6.9 7.4.7-5.6 5 1.7 7.4L12 17.7l-6.6 3.8 1.7-7.4-5.6-5 7.4-.7z"/></svg>
      </div>
      <h1 class="brand-name">CEDAR HOLLOW</h1>
      <h2 class="wine-style">RED BLEND</h2>
      <div class="vineyard-scene" role="img" aria-label="Silver engraved sketch of a hillside vineyard with a farmhouse, cypress trees and rows of vines"></div>
      <p class="grape-varieties">MERLOT | CARBERNET SAUVIGNON<br>CARBERNET FRANC | PETIT VERDOT | MALBEC</p>
      <div class="divider"></div>
      <p class="vintage">2018</p>
    </section>
  </main>
</body>
</html>
```